Portal for Beautiful & Up-and-Coming Caribbean destination of KVT, Puerto Rico

We need the web design of an online portal for the KVT community of Puerto Rico. This should include the landing page, menu page, and at least one content page. The KVT area is a vibrant area in Northwest Puerto Rico with an airport, many local restaurants, beautiful beaches, and many things to do. I attach the logo which should be featured prominently, and we'll also be selling merchandise using this logo. The website should be a place for everyone in the community or tourists looking for things to do and places to stay. It will need to feature space and places for advertising as well. Also, we have a live hashtag feed (www.kvtvibe-demo.com) where businesses and people in the community can hashtag their posts (we have licensed software that updates it every 30 minutes). We would like for the live hashtag feed to be part of the design, though the format can be changed a bit from what is currently in place. Indeed, the landing page should be changed to emphasize both the hashtag feed as well as the content of the site of KVTvibe. We need the landing page, menu page which will include 10-15 different modules or pages (examples: restaurants, things to do, places to stay, flights). I attach a spreadsheet which shows the menu pages that need to be featured. Comparable websites in our area are www.gosulena.com and www.varelaguide.com (but I don't like either one!). The final design should be contemporary, fresh, colorful fun and current, and communicate a vibrant and interactive community.

Target Market(s)

Tourists and people who live in this beach - oriented, beautiful community

Industry/Entity Type

Community

Number of Pages Required

3 page

Font styles to use
Sans Serif

Colors
33a6d7
f68e4e

Requirements
Must have
• landing page, menu design/page, and a sample content page. It must integrate a live hashtag feed, comparable to what is currently seen on www.kvtvibe-demo.com. It must be fun, contemporary, colorful, unique, and clean. It must allow for advertising space.
Nice to have
• comments and interaction with visitors. Colors that integrate with the logo. Much emphasis on the logo, as we will also be selling merchandise.
Should not have
• extra squiggles and curlies and adornments.

```html
<!DOCTYPE html>
<html lang="en">
<head>
<meta charset="utf-8">
<title>KVTvibe — Menu</title>
<link href="https://fonts.googleapis.com/css2?family=Inter:wght@300;400;600;700&display=swap" rel="stylesheet">
<style>
  :root {
    --brand-blue: #33a6d7;
    --brand-orange: #f68e4e;
    --ink: #1b1b1b;
    --muted: #8a8a8a;
    --link: #2aa3e6;
    --row-black: #000000;
    --row-dark: #1f2a30;
    --row-restaurants: #29b6e6;
    --row-entertainment: #2aa0e8;
    --row-stay: #2b88ea;
    --row-science: #2c70e9;
    --row-involved: #3058e6;
    --row-beaches: #3a42e0;
    --row-surf: #583fe0;
    --row-realestate: #763fe2;
    --row-historical: #9640e2;
    --row-shopping: #b23fe0;
    --row-partners: #3b8fe8;
  }
  * { box-sizing: border-box; margin: 0; padding: 0; }
  html, body { width: 1200px; height: 900px; overflow: hidden; background: #fff; }
  body { font-family: "Inter", "Helvetica Neue", Arial, sans-serif; }

  .page { position: relative; width: 1200px; height: 900px; display: flex; }

  /* Hero */
  .hero { position: relative; width: 754px; height: 900px; overflow: hidden; }
  .hero__photo {
    position: absolute; inset: 0;
    background: linear-gradient(180deg, #1f5fae 0%, #4a8fd0 22%, #9cc4e6 42%, #d9e9f4 55%, #2e8aa6 60%, #4ea8b8 64%, #d8c9a6 70%, #e7d8b6 100%);
  }
  .hero__boats {
    position: absolute; left: 0; top: 530px; width: 754px; height: 150px;
    background: linear-gradient(90deg, #c9443a 0%, #d9b13c 40%, #c23a2f 65%, #2f7a6a 100%);
    opacity: .75;
  }
  .logo-disc {
    position: absolute; left: 185px; top: 97px; width: 360px; height: 360px;
    border-radius: 50%; background: #fff;
    display: flex; align-items: center; justify-content: center;
  }
  .logo-disc__name {
    font-size: 64px; font-weight: 400; color: var(--brand-orange); letter-spacing: 1px;
  }

  /* Hashtag feed */
  .feed {
    position: absolute; left: 70px; top: 652px; width: 613px; height: 248px;
    background: rgba(255,255,255,.55); padding: 14px 16px 0;
  }
  .feed__list { background: #fff; height: 100%; }
  .post {
    position: relative; display: flex; gap: 12px;
    padding: 12px 12px 10px 12px; border-bottom: 1px solid #e6e6e6;
  }
  .post__avatar { flex: none; width: 54px; height: 54px; border-radius: 4px; }
  .post__avatar--teal { background: linear-gradient(135deg, #7ed6d0, #3fb0b8); }
  .post__avatar--grey { background: linear-gradient(135deg, #a8a8a8, #505050); }
  .post__body { font-size: 15px; line-height: 21px; color: var(--ink); }
  .post__name { font-weight: 700; }
  .post__handle { color: var(--muted); font-size: 13px; }
  .post__mention { color: var(--link); }
  .post__strong { font-weight: 600; }
  .post__link { color: var(--link); display: block; }
  .post__meta { color: var(--link); font-size: 13px; }
  .post__meta--grey { color: var(--muted); }
  .post__time { position: absolute; right: 12px; top: 10px; font-size: 13px; color: var(--muted); }

  /* Menu */
  .menu { width: 446px; height: 900px; display: flex; flex-direction: column; }
  .menu__item {
    display: flex; align-items: center; height: 65px; color: #fff;
    font-size: 25px; font-weight: 300; text-decoration: none;
  }
  .menu__item--head { height: 80px; background: var(--row-black); }
  .menu__icon { width: 150px; display: flex; justify-content: center; padding-right: 4px; }
  .menu__icon svg { width: 44px; height: 44px; fill: none; stroke: #fff; stroke-width: 1.8; stroke-linecap: round; stroke-linejoin: round; }
  .menu__partners {
    flex: 1; display: flex; align-items: center; background: var(--row-partners);
    color: #fff; font-size: 25px; font-weight: 300; padding-left: 30px; gap: 22px;
  }
  .partner-badge { width: 50px; height: 50px; border-radius: 50%; background: #fff; }
  .menu__partners span { margin-left: 0; }
</style>
</head>
<body>
<div class="page">
  <section class="hero">
    <div class="hero__photo" role="img" aria-label="Photo of a Caribbean beach with colourful wooden fishing boats under a blue sky"></div>
    <div class="hero__boats" role="img" aria-label="Colourful fishing boats resting on the sand"></div>

    <div class="logo-disc">
      <span class="logo-disc__name">KVTvibe</span>
    </div>

    <aside class="feed" aria-label="Live hashtag feed">
      <div class="feed__list">
        <article class="post">
          <div class="post__avatar post__avatar--teal" role="img" aria-label="User avatar"></div>
          <div class="post__body">
            <span class="post__name">marisolr</span> <span class="post__handle">@marisolr</span><br>
            This Tweet from <span class="post__mention">@marisolr</span> <span class="post__strong">has been withheld in response to a report from the copyright holder.</span> Learn more:
            <span class="post__link">help.feedhub-demo.com/articles/2048#</span>
            <span class="post__meta">&#9643; View summary</span>
          </div>
          <span class="post__time">1h</span>
        </article>
        <article class="post">
          <div class="post__avatar post__avatar--grey" role="img" aria-label="User avatar"></div>
          <div class="post__body">
            <span class="post__name">Tomas Quiles</span> <span class="post__handle">@tquiles</span><br>
            This Tweet from <span class="post__mention">@tquiles</span> <span class="post__strong">has been withheld in response to a report from the copyright holder.</span> Learn more:
            <span class="post__link">sunsetwaves-demo.net</span>
            <span class="post__meta post__meta--grey">Expand</span>
          </div>
          <span class="post__time">1h</span>
        </article>
      </div>
    </aside>
  </section>

  <nav class="menu">
    <a class="menu__item menu__item--head">
      <span class="menu__icon"><svg viewBox="0 0 44 44"><path d="M8 36a14 14 0 0 1 28 0"/><path d="M16 36c0-5 3-8 6-8s6 3 6 8"/><path d="M18 12l8 0M22 8l4 4-4 4"/><path d="M6 22q4-10 16-12M38 22q-3-8-10-11" stroke-dasharray="2 3"/></svg></span>
      Getting here and away</a>
    <a class="menu__item" style="background:var(--row-dark)">
      <span class="menu__icon"><svg viewBox="0 0 44 44"><rect x="6" y="8" width="32" height="30"/><path d="M6 15h32M13 5v6M31 5v6M6 22h32M6 29h32M14 15v23M22 15v23M30 15v23"/></svg></span>
      Events Calendar</a>
    <a class="menu__item" style="background:var(--row-restaurants)">
      <span class="menu__icon"><svg viewBox="0 0 44 44"><circle cx="22" cy="22" r="11"/><circle cx="22" cy="22" r="7"/><path d="M5 10v10M8 10v10M5 20h3M6.5 20v14M39 10v24M39 10q-4 6 0 12"/></svg></span>
      Restaurants</a>
    <a class="menu__item" style="background:var(--row-entertainment)">
      <span class="menu__icon"><svg viewBox="0 0 44 44"><path d="M6 14q10-4 18 0v10a9 9 0 0 1-18 0z"/><path d="M20 11q8-3 18 1v9a9 9 0 0 1-12 8"/><path d="M10 27q5 4 10 0M27 21q4-3 8 0"/></svg></span>
      Live Entertainment</a>
    <a class="menu__item" style="background:var(--row-stay)">
      <span class="menu__icon"><svg viewBox="0 0 44 44"><path d="M4 10v26M40 20v16M4 28h36M4 22h36"/><rect x="8" y="15" width="8" height="5"/></svg></span>
      Places to stay</a>
    <a class="menu__item" style="background:var(--row-science)">
      <span class="menu__icon"><svg viewBox="0 0 44 44"><ellipse cx="22" cy="22" rx="18" ry="7"/><ellipse cx="22" cy="22" rx="18" ry="7" transform="rotate(60 22 22)"/><ellipse cx="22" cy="22" rx="18" ry="7" transform="rotate(120 22 22)"/><circle cx="22" cy="22" r="3"/></svg></span>
      Science</a>
    <a class="menu__item" style="background:var(--row-involved)">
      <span class="menu__icon"><svg viewBox="0 0 44 44"><path d="M22 20l-6-6a4 4 0 0 1 6-5 4 4 0 0 1 6 5z"/><path d="M4 28h3v10H4M7 30h9l9 2a2 2 0 0 1 0 4h-8M7 36l10 2 18-6a2 2 0 0 0-2-4l-8 2"/></svg></span>
      Get Involved</a>
    <a class="menu__item" style="background:var(--row-beaches)">
      <span class="menu__icon"><svg viewBox="0 0 44 44"><path d="M6 14q10-10 20 0zM16 14v14"/><circle cx="34" cy="12" r="4"/><path d="M4 28h36M8 33h8M22 33h12M6 38h4M16 38h6M28 38h10" stroke-dasharray="2 2"/></svg></span>
      Map of Beaches</a>
    <a class="menu__item" style="background:var(--row-surf)">
      <span class="menu__icon"><svg viewBox="0 0 44 44"><path d="M12 40q-8-16 4-34 8 16-4 34z"/><path d="M22 36q6-18 16-30 4 16-16 30z"/></svg></span>
      Surf and Wind Reports</a>
    <a class="menu__item" style="background:var(--row-realestate)">
      <span class="menu__icon"><svg viewBox="0 0 44 44"><path d="M14 14l9-8 9 8v10H14z"/><rect x="20" y="16" width="6" height="5"/><path d="M4 28h3v10H4M7 30h9l9 2a2 2 0 0 1 0 4h-8M7 36l10 2 18-6a2 2 0 0 0-2-4l-8 2"/></svg></span>
      Real Estate</a>
    <a class="menu__item" style="background:var(--row-historical)">
      <span class="menu__icon"><svg viewBox="0 0 44 44"><path d="M22 4v6M18 16l4-6 4 6zM16 16h12v8H16zM12 24h20v12H12zM6 38h32M18 36v-6h8v6"/></svg></span>
      Historical Sites</a>
    <a class="menu__item" style="background:var(--row-shopping)">
      <span class="menu__icon"><svg viewBox="0 0 44 44"><rect x="6" y="14" width="22" height="24"/><path d="M12 14v-4a5 5 0 0 1 10 0v4"/><rect x="22" y="22" width="16" height="16"/><path d="M26 22v-3a4 4 0 0 1 8 0v3"/></svg></span>
      Shopping</a>
    <div class="menu__partners">
      <span class="partner-badge" aria-label="Partner"></span>
      <span class="partner-badge" aria-label="Partner"></span>
      <span>Logos colaboradores</span>
    </div>
  </nav>
</div>
</body>
</html>
```